New flyer design for construction company marketing and description of services.

I want to have a flyer design that my techs will carry to deliver after job completion or for marketing purposes, to explain what services we provide, we offer General construction services.

Brellor Homecraft Sevices originated from a family-owned and operated contractor business, performing home renovation, addition, and construction work in the NYC area since 2004.

Today, we specialize in reliable and affordable Construction services for residential and commercial clients In 2014, we expanded to northern New Jersey. In 2016, we brought quality home improvement and repair services to new Bucks County, PA, and nearby New Jersey areas.
We offer carpentry, electrical, plumbing, renovation, remodel, cleaning services and landscaping.
I would like to have a section for home rental maintenance.

Target Market(s)

Homeowners, rental properties, real state and Senior citizen

Industry/Entity Type

Construction Company

Colors

Designer to choose colors to be used in the design.

Requirements
Must have
• A special design that will attract 55 + clients maybe a logo version that will be more attractive to seniors. I would updated the briefing with design and previous pictures, but we have all available in our social media instagram and facebook:
• https://www.pictogram.example/brellorhomecraft/?hl=en
• https://www.friendsbook.example/brellorhome/
Nice to have
• New design ideas and layouts.

```html
<!DOCTYPE html>
<html lang="en">
<head>
<meta charset="utf-8">
<title>Services Flyer</title>
<link href="https://fonts.googleapis.com/css2?family=Oswald:wght@500;600&family=Open+Sans:wght@400&display=swap" rel="stylesheet">
<style>
  :root {
    --red: #d9232a;
    --yellow: #f6c21c;
    --ink: #111111;
    --body: #555555;
    --paper: #ffffff;
    --cream: #f7efc4;
  }
  * { margin: 0; padding: 0; box-sizing: border-box; }
  html, body { width: 847px; height: 1200px; overflow: hidden; background: var(--paper); }
  .flyer { position: relative; width: 847px; height: 1200px; overflow: hidden; background: var(--paper); font-family: "Open Sans", Arial, sans-serif; }
  .backdrop { position: absolute; inset: 0; }
  .service { position: absolute; width: 390px; }
  .service-title { display: flex; align-items: center; gap: 12px; font-family: "Oswald", "Arial Narrow", sans-serif; font-weight: 600; font-size: 27px; line-height: 1.2; color: var(--red); text-transform: uppercase; letter-spacing: 0.3px; margin-bottom: 8px; }
  .service-title svg { width: 30px; height: 30px; flex: none; }
  .service-copy { font-size: 13px; line-height: 1.55; color: var(--body); }
  .general { left: 44px; top: 330px; }
  .maintenance { left: 44px; top: 540px; }
  .cleaning { left: 44px; top: 750px; }
  .handyman { left: 478px; top: 968px; width: 340px; }
  .badge { position: absolute; left: 490px; top: 575px; width: 180px; text-align: center; font-family: "Oswald", "Arial Narrow", sans-serif; font-weight: 500; font-size: 32px; line-height: 1.15; color: var(--cream); text-transform: uppercase; }
</style>
</head>
<body>
<main class="flyer">
  <svg class="backdrop" width="847" height="1200" viewBox="0 0 847 1200">
    <defs>
      <linearGradient id="goldFill" x1="0" y1="0" x2="1" y2="1">
        <stop offset="0" stop-color="#fbd54a"/>
        <stop offset="1" stop-color="#e3a40c"/>
      </linearGradient>
      <linearGradient id="siteTones" x1="0" y1="0" x2="1" y2="1">
        <stop offset="0" stop-color="#cfd9e2"/>
        <stop offset="0.45" stop-color="#c89c63"/>
        <stop offset="1" stop-color="#8a6a45"/>
      </linearGradient>
    </defs>
    <polygon points="0,0 440,0 300,150 0,290" fill="url(#goldFill)" role="img" aria-label="Faceted yellow and grey geometric pattern"/>
    <polygon points="0,0 180,0 0,120" fill="#d8d8d8" opacity="0.55"/>
    <polygon points="440,0 847,0 847,820 640,950 500,850 580,470" fill="url(#siteTones)" role="img" aria-label="Photo of a handyman cutting lumber with a miter saw at a framing job site"/>
    <polyline points="440,0 580,470 500,850" fill="none" stroke="var(--red)" stroke-width="5"/>
    <polyline points="500,850 640,950 847,820" fill="none" stroke="var(--red)" stroke-width="5"/>
    <polyline points="360,1200 500,850" fill="none" stroke="var(--red)" stroke-width="3"/>
    <rect x="500" y="560" width="160" height="160" transform="rotate(45 580 640)" fill="var(--ink)" stroke="var(--red)" stroke-width="6"/>
  </svg>

  <div class="badge">Licensed<br>and<br>Insured</div>

  <section class="service general">
    <h2 class="service-title">
      <svg viewBox="0 0 34 34"><path d="M22 4a8 8 0 0 0-7.5 10.6L4 25.1 8.9 30l10.5-10.5A8 8 0 0 0 30 12l-5 5-5-1-1-5 5-5z" fill="var(--red)"/></svg>
      General Contractor
    </h2>
    <p class="service-copy">We work on an hourly basis. Our rates are $70.00 per hour with a 3 hour minimum ($210.00) per handyman. So, if we come to your location to perform a job, the minimum charge will be $210, and you will have three hours of time for us to complete whatever jobs you would like. If a helper is required, the minimum hourly rate is $100, and minimum visit rate is $230.</p>
  </section>

  <section class="service maintenance">
    <h2 class="service-title">
      <svg viewBox="0 0 34 34"><path d="M17 4 3 16h4v14h8v-8h4v8h8V16h4z" fill="var(--red)"/></svg>
      Property Maintenance
    </h2>
    <p class="service-copy">We work on an hourly basis. Our rates are $70.00 per hour with a 3 hour minimum ($210.00) per handyman. So, if we come to your location to perform a job, the minimum charge will be $210, and you will have three hours of time for us to complete whatever jobs you would like. If a helper is required, the minimum hourly rate is $100, and minimum visit rate is $230.</p>
  </section>

  <section class="service cleaning">
    <h2 class="service-title">
      <svg viewBox="0 0 34 34"><path d="M12 3h9v5h-9zM11 9h11l2 6v16H9V15z" fill="var(--red)"/><path d="M21 4h6v3h-6z" fill="var(--red)"/></svg>
      Cleaning Services
    </h2>
    <p class="service-copy">We work on an hourly basis. Our rates are $70.00 per hour with a 3 hour minimum ($210.00) per handyman. So, if we come to your location to perform a job, the minimum charge will be $210, and you will have three hours of time for us to complete whatever jobs you would like. If a helper is required, the minimum hourly rate is $100, and minimum visit rate is $230.</p>
  </section>

  <section class="service handyman">
    <h2 class="service-title">
      <svg viewBox="0 0 34 34"><circle cx="17" cy="17" r="13" fill="none" stroke="var(--red)" stroke-width="4"/><path d="M9 25 25 9" stroke="var(--red)" stroke-width="4"/></svg>
      Handyman Services
    </h2>
    <p class="service-copy">We work on an hourly basis. Our rates are $70.00 per hour with a 3 hour minimum ($210.00) per handyman. So, if we come to your location to perform a job, the minimum charge will be $210, and you will have three hours of time for us to complete whatever jobs you would like. If a helper is required, the minimum hourly rate is $100, and minimum visit rate is $230.</p>
  </section>
</main>
</body>
</html>
```